sailbrightly Website for children with diabilities

Hi, we are looking for a new website design for our community service "sailbrightly". Sailbrightly gives children who suffer from diseases or disabilities a week off on a Boat to give the children new hope and an unforgettable experience.

The current website is really old and we want to have a new one.
Please feel free to discover our website under http://sailbrightly-example.at/.
We have several company sponsors which are very important to us.

The Website has to be a Bootstrap Design (Version 4.4 or higher) [NOT Wordpress, Joomla, other CMS]

Target Market(s)

no target market. we like to inform our communities about our service.

Industry/Entity Type

community service for children with disabilities

Coding

Number of Pages Required

4 page

Font styles to use
Sans Serif

Colors
0054AA
0677BA
7BADD7
CADEEF
E8F1F8
0094D4
00A9DD
6FCCEA
C7EBF8
E9F6FB

Requirements
Must have
• About, Sponsors, Information about cruises
Nice to have
• Gallery

```html
<!DOCTYPE html>
<html lang="en">
<head>
<meta charset="utf-8">
<title>Sailbrightly</title>
<link href="https://fonts.googleapis.com/css2?family=Fredoka:wght@600;700&family=Poppins:wght@400;500;600;700&display=swap" rel="stylesheet">
<style>
:root{
  --blue-deep:#0054AA;
  --blue:#0677BA;
  --blue-bright:#0094D4;
  --blue-sky:#00A9DD;
  --blue-light:#7BADD7;
  --blue-pale:#CADEEF;
  --blue-mist:#E8F1F8;
  --ink:#111111;
  --text:#555555;
  --white:#ffffff;
  --rule:#e4e4e4;
}
*{box-sizing:border-box;margin:0;padding:0}
html,body{width:1200px;height:3645px;overflow:hidden}
body{position:relative;font-family:"Poppins",sans-serif;color:var(--text);background:var(--white)}
.abs{position:absolute}
.display{font-family:"Fredoka",sans-serif;font-weight:700;color:var(--ink);line-height:1}
.accent{color:var(--blue-bright)}

/* hero */
.hero{left:0;top:0;width:1200px;height:686px;background:linear-gradient(100deg,#59687a 0%,#8a96a3 35%,#a9b6c2 60%,#7f8f9e 100%)}
.hero-photo{position:absolute;inset:0}
.brand{font-family:"Poppins",sans-serif;font-weight:700;font-size:34px;letter-spacing:-0.5px;line-height:1}
.hero .brand{left:120px;top:46px;color:var(--white)}
.nav{top:66px;display:flex;gap:0;font-size:12.5px;font-weight:500;color:var(--ink)}
.nav a{position:absolute;white-space:nowrap;color:#111;text-decoration:none}
.hero-kicker{left:114px;top:242px;font-size:54px;color:var(--blue-bright)}
.hero-title{left:114px;top:300px;font-size:92px;color:var(--white)}
.hero-text{left:115px;top:418px;width:490px;font-size:12.5px;line-height:21px;color:var(--white)}

/* about */
.about-frame{left:140px;top:850px;width:391px;height:489px;border:3px solid var(--ink);border-radius:10px}
.about-photo{left:157px;top:869px;width:391px;height:489px;border-radius:10px;background:linear-gradient(150deg,#dfe6ea 0%,#b9c9d2 45%,#7a95ad 75%,#d8cfc4 100%)}
.about-title{left:644px;top:900px;font-size:58px}
.about-sub{left:636px;top:978px;font-size:15px;font-weight:600;color:var(--ink)}
.body-copy{font-size:13.5px;line-height:25.7px;color:var(--text)}
.about-copy{left:635px;width:440px}

/* goals */
.goals-band{left:0;top:1504px;width:1200px;height:470px;background:linear-gradient(180deg,#0a7cc2 0%,#1389d0 100%)}
.goals-title{left:0;top:1578px;width:1200px;text-align:center;font-size:60px;color:var(--white)}
.goals-sub{left:0;top:1652px;width:1200px;text-align:center;font-size:13.5px;line-height:26px;color:var(--white)}
.card{top:1760px;width:276px;height:382px;border:2px solid var(--blue-bright);border-radius:12px;background:var(--white);overflow:hidden}
.card-photo{height:214px}
.card h3{position:absolute;left:45px;top:253px;font-size:15px;font-weight:600;color:var(--ink)}
.card p{position:absolute;left:45px;top:295px;width:180px;font-size:13.5px;line-height:26px;color:var(--text)}

/* sponsors */
.sponsor{top:2226px;height:38px;display:flex;align-items:center;justify-content:center;font-weight:700;font-size:20px;white-space:nowrap}
.arrow{top:2235px}
.rule{left:120px;top:2342px;width:951px;height:1px;background:var(--rule)}

/* cruises */
.cruise-title{left:143px;top:2515px;font-size:58px}
.cruise-copy{left:143px;width:520px}
.cruise-photo{left:740px;top:2377px;width:305px;height:541px;border-radius:150px 150px 20px 20px;background:linear-gradient(180deg,#6b4a34 0%,#c9c4bd 30%,#b8b2aa 60%,#3a3a3a 100%)}

/* gallery */
.gallery{left:0;top:2918px;width:1200px;height:228px;display:flex}
.tile{width:240px;height:228px;position:relative}
.tile-feature{background:linear-gradient(160deg,#1e8fd8 0%,#0d7fc8 100%)}
.tile-feature h4{position:absolute;left:36px;top:121px;font-size:18px;font-weight:600;color:var(--white)}
.tile-feature p{position:absolute;left:36px;top:161px;width:180px;font-size:11.5px;line-height:19px;color:var(--white)}
.tile-feature svg{position:absolute;left:181px;top:26px}

/* footer */
.footer .brand{left:120px;top:3240px;color:var(--ink);font-size:36px}
.foot-text{left:120px;top:3309px;width:260px;font-size:12px;line-height:25.6px;color:var(--text)}
.social{top:3412px;width:28px;height:28px;border-radius:50%;background:var(--blue-bright)}
.foot-head{top:3256px;font-size:18px;font-weight:700;color:var(--ink)}
.contact-row{left:512px;display:flex;font-size:12px;line-height:25.6px;color:var(--text)}
.contact-row svg{position:absolute;left:0;top:4px}
.contact-row span{margin-left:29px}
.pages{left:931px;top:3315px;list-style:none;font-size:12px;line-height:31px;color:var(--text)}
.bottom-bar{left:0;top:3587px;width:1200px;height:58px;background:var(--blue-bright);color:var(--white);font-size:12px;display:flex;align-items:center;justify-content:center;gap:8px}
</style>
</head>
<body>

<header class="hero abs">
  <div class="hero-photo" role="img" aria-label="Photo of two children hugging on the deck of a sailing boat on the lake"></div>
  <div class="brand abs">Sailbrightly</div>
  <nav class="nav abs" style="left:0;width:1200px">
    <a style="left:823px">Home</a>
    <a style="left:897px">sponsors</a>
    <a style="left:990px">Fleet Info 2022</a>
  </nav>
  <div class="hero-kicker display abs">Unforgettable</div>
  <h1 class="hero-title display abs">Experience</h1>
  <p class="hero-text abs">Sailbrightly association and organize a fleet for socially disadvantaged children and young people from central Upper Austria every year and set up the necessary financial resources.</p>
</header>

<section class="about">
  <div class="about-photo abs" role="img" aria-label="Photo of two children in sunglasses lying on a blanket on deck holding a toy plane"></div>
  <div class="about-frame abs"></div>
  <h2 class="about-title display abs">About <span class="accent">Us</span></h2>
  <p class="about-sub abs">New hope and an unforgettable experience</p>
  <p class="about-copy body-copy abs" style="top:1044px">We want enabling children and young people who don't always have it easy in life to spend an unforgettable week in Croatia. It is precisely this shared experience that gives the children and young people a new zest for life and perspectives for their future.</p>
  <p class="about-copy body-copy abs" style="top:1198px">Through the reflection and also the care afterwards in the individual facilities, the children and young people can draw on this experience for a long time to come. This sustainability creates numerous pedagogical points of contact that represent a valuable basis for the achievement of goals.</p>
</section>

<section class="goals">
  <div class="goals-band abs" role="img" aria-label="Faded blue-tinted photo of people on a boat"></div>
  <h2 class="goals-title display abs">Project Goals</h2>
  <p class="goals-sub abs">Lorem ipsum dolor sit amet, consectetur adipiscing elit. Ut aliquam egestas sagittis.<br>Pellentesque egestas consectetur turpis non elementum.</p>

  <article class="card abs" style="left:141px">
    <div class="card-photo" role="img" aria-label="Photo of two smiling children on a boat" style="background:linear-gradient(160deg,#e9ecef 0%,#9fb1c4 50%,#3f6a9a 100%)"></div>
    <h3>Self Esteem and Skills</h3>
    <p>Lorem ipsum dolor sit amet, consectetur</p>
  </article>
  <article class="card abs" style="left:461px">
    <div class="card-photo" role="img" aria-label="Photo of a girl with a flower crown on a boat" style="background:linear-gradient(160deg,#d9dee3 0%,#8d9aa6 50%,#4d5a44 100%)"></div>
    <h3>Take Responsibility</h3>
    <p>Lorem ipsum dolor sit amet, consectetur</p>
  </article>
  <article class="card abs" style="left:780px">
    <div class="card-photo" role="img" aria-label="Photo of a girl lying on a boat deck in sunglasses" style="background:linear-gradient(160deg,#e6eaee 0%,#b8c4cf 50%,#6d88a6 100%)"></div>
    <h3>Practicing Tolerance</h3>
    <p>Lorem ipsum dolor sit amet, consectetur</p>
  </article>
</section>

<section class="sponsors">
  <svg class="arrow abs" style="left:116px" width="12" height="20" viewBox="0 0 12 20"><path d="M10 2 2 10l8 8" fill="none" stroke="#333" stroke-width="1.8"/></svg>
  <div class="sponsor abs" style="left:170px;width:180px;color:#2e7d6e">Hollmann</div>
  <div class="sponsor abs" style="left:410px;width:180px;color:#111">Brentwick</div>
  <div class="sponsor abs" style="left:630px;width:170px;color:#1b5fa6">Voltara Elektro</div>
  <div class="sponsor abs" style="left:845px;width:170px;color:#1b6fae">Lindmar Reisen</div>
  <svg class="arrow abs" style="left:1060px" width="12" height="20" viewBox="0 0 12 20"><path d="M2 2l8 8-8 8" fill="none" stroke="#333" stroke-width="1.8"/></svg>
  <div class="rule abs"></div>
</section>

<section class="cruises">
  <h2 class="cruise-title display abs">About <span class="accent">Cruises</span></h2>
  <p class="cruise-copy body-copy abs" style="top:2607px">Lorem ipsum dolor sit amet, consectetur adipiscing elit. Ut aliquam egestas sagittis. Pellentesque egestas consectetur turpis non elementum.</p>
  <p class="cruise-copy body-copy abs" style="top:2685px">Pellentesque habitant morbi tristique senectus et netus et malesuada fames ac turpis egestas. Phasellus aliquam sodales lacinia.</p>
  <div class="cruise-photo abs" role="img" aria-label="Cut-out photo of a curly-haired child holding a toy sailboat"></div>
</section>

<section class="gallery abs">
  <div class="tile" role="img" aria-label="Photo of a girl with a flower crown at the helm" style="background:linear-gradient(160deg,#5d6e7d 0%,#8b97a0 50%,#3e4a52 100%)"></div>
  <div class="tile" role="img" aria-label="Photo of a smiling girl in a life jacket" style="background:linear-gradient(160deg,#4d5d6a 0%,#c9a99a 55%,#d0675c 100%)"></div>
  <div class="tile" role="img" aria-label="Photo of a man and a boy looking out over the water" style="background:linear-gradient(160deg,#9aa3ab 0%,#c74b3a 50%,#d9d9d9 100%)"></div>
  <div class="tile tile-feature">
    <svg width="26" height="26" viewBox="0 0 26 26"><circle cx="11" cy="11" r="8.5" fill="none" stroke="#fff" stroke-width="1.6"/><path d="M17.5 17.5 24 24" stroke="#fff" stroke-width="1.6"/></svg>
    <h4>Mara Lind</h4>
    <p>Lorem Ipsum is simply dummy text of the printing</p>
  </div>
  <div class="tile" role="img" aria-label="Photo of a boy sitting at the rail looking at the lake" style="background:linear-gradient(160deg,#6f8496 0%,#4d6073 50%,#2a4c86 100%)"></div>
</section>

<footer class="footer">
  <div class="brand abs">Sailbrightly</div>
  <p class="foot-text abs">Lorem ipsum dolor sit amet, consectetur adipisicing elit, sed do eiusmod tempor incididunt ut labore et dolore</p>
  <span class="social abs" style="left:122px" aria-label="Social link"></span>
  <span class="social abs" style="left:162px" aria-label="Social link"></span>
  <span class="social abs" style="left:201px" aria-label="Social link"></span>
  <span class="social abs" style="left:241px" aria-label="Social link"></span>

  <h4 class="foot-head abs" style="left:502px">Contact</h4>
  <div class="contact-row abs" style="top:3309px">
    <svg width="16" height="18" viewBox="0 0 16 18"><path d="M8 17s6-6 6-10A6 6 0 0 0 2 7c0 4 6 10 6 10z" fill="none" stroke="#0094D4" stroke-width="1.3"/><circle cx="8" cy="7" r="2.2" fill="none" stroke="#0094D4" stroke-width="1.3"/></svg>
    <span>Address:<br>14 Harbour Lane, 4020 Linz,<br>Austria</span>
  </div>
  <div class="contact-row abs" style="top:3413px">
    <svg width="16" height="16" viewBox="0 0 16 16"><path d="M3 1.5h3l1.5 3.5-2 1.2a8 8 0 0 0 4.3 4.3l1.2-2 3.5 1.5v3A1.5 1.5 0 0 1 13 14.5 12 12 0 0 1 1.5 3 1.5 1.5 0 0 1 3 1.5z" fill="none" stroke="#0094D4" stroke-width="1.2"/></svg>
    <span>Phone: +43 123-456-7890</span>
  </div>
  <div class="contact-row abs" style="top:3439px">
    <svg width="16" height="16" viewBox="0 0 16 16"><rect x="4" y="1.5" width="8" height="4" fill="none" stroke="#0094D4" stroke-width="1.2"/><rect x="1.5" y="5.5" width="13" height="6" rx="1" fill="none" stroke="#0094D4" stroke-width="1.2"/><rect x="4" y="9.5" width="8" height="5" fill="#fff" stroke="#0094D4" stroke-width="1.2"/></svg>
    <span>Fax: +43 123-456-7891</span>
  </div>
  <div class="contact-row abs" style="top:3465px">
    <svg width="16" height="16" viewBox="0 0 16 16"><rect x="1.5" y="3" width="13" height="10" fill="none" stroke="#0094D4" stroke-width="1.2"/><path d="M1.5 3 8 9l6.5-6" fill="none" stroke="#0094D4" stroke-width="1.2"/></svg>
    <span>Email: info@sailbrightly-example.at</span>
  </div>
  <div class="contact-row abs" style="top:3491px">
    <svg width="16" height="16" viewBox="0 0 16 16"><circle cx="8" cy="8" r="6.5" fill="none" stroke="#0094D4" stroke-width="1.2"/><ellipse cx="8" cy="8" rx="3" ry="6.5" fill="none" stroke="#0094D4" stroke-width="1.2"/><path d="M1.5 8h13" stroke="#0094D4" stroke-width="1.2"/></svg>
    <span>Website: sailbrightly-example.at</span>
  </div>

  <h4 class="foot-head abs" style="left:931px">Pages</h4>
  <ul class="pages abs">
    <li>Home</li>
    <li>About Us</li>
    <li>Services</li>
    <li>FAQ</li>
    <li>Testimonials</li>
  </ul>

  <div class="bottom-bar abs">
    <span>© Sailbrightly 2022</span><span>|</span><span>Terms of Use</span><span>|</span><span>Membership Terms &amp; Conditions</span><span>|</span><span>Privacy Policy</span>
  </div>
</footer>

</body>
</html>
```